Wordpress Theme for Martial Arts School

Need a new theme for our website. Looking to update the look and feel of it. Bring it up to date with a clean and bold look.

Target Market(s)

Parents

Industry/Entity Type

School

Requirements
Must have
• See attached sketch

Sliding Billboard Header

Program Boxes in Footer

Glimmerpad, Plovik, and Zentaro Social Icons

Logo in middle of menu

Pay no attention to the colors in the sketch work off of the colors in the logo.

Nice to have
• or you could Ignore everything I said and blow me away with something completely different and creative.

```html
<!DOCTYPE html>
<html lang="en">
<head>
<meta charset="utf-8">
<title>Ironleaf Dojo</title>
<link rel="stylesheet" href="https://fonts.googleapis.com/css2?family=Arimo:wght@400;700&family=Noto+Serif:ital@0;1&family=Open+Sans:wght@400;600&display=swap">
<style>
:root{
  --dark:#262626;
  --darker:#0d0d0d;
  --red:#b0141c;
  --deep-red:#8a0e14;
  --pink:#d59aa0;
  --light:#f2f2f2;
  --panel:#e6e6e6;
  --grey-text:#7a7f88;
  --white:#ffffff;
  --sky:#5d8fc9;
  --footer-grey:#9a9a9a;
}
*{margin:0;padding:0;box-sizing:border-box}
html,body{width:1182px;height:1200px;overflow:hidden;background:var(--dark)}
.page{position:relative;width:1182px;height:1200px;overflow:hidden;font-family:Arimo,Arial,sans-serif}
.abs{position:absolute}

.header{left:0;top:0;width:1182px;height:430px;background:radial-gradient(ellipse at 50% 30%,#353535,var(--dark) 70%)}
.nav a{position:absolute;top:58px;color:#e6e6e6;font-weight:700;font-size:13px;text-decoration:none;letter-spacing:.2px}
.nav .schedule{top:46px;left:764px;width:106px;height:36px;padding:12px 0 0 10px;color:#333;background:linear-gradient(#fff,#dcdcdc);border-radius:8px 8px 0 0}
.nav .schedule span{color:var(--red);margin-left:6px;font-size:10px}
.brand{left:393px;top:30px;width:352px;height:80px;display:flex;align-items:center;justify-content:center;gap:12px}
.brand-dot{width:16px;height:16px;border-radius:50%;background:var(--red)}
.brand-name{font-family:"Noto Serif",Georgia,serif;color:var(--white);font-size:34px;letter-spacing:1px}

.slider-frame{left:155px;top:109px;width:873px;height:277px;background:linear-gradient(#bdbdbd,#7c7c7c);box-shadow:0 10px 25px rgba(0,0,0,.5)}
.slider-mat{left:164px;top:118px;width:854px;height:259px;background:var(--white)}
.slide-photo{left:170px;top:127px;width:836px;height:241px;background:linear-gradient(180deg,#3f74b8 0%,var(--sky) 45%,#cfdced 75%,#eef2f6 100%)}
.slide-title{left:184px;top:136px;font-family:"Noto Serif",Georgia,serif;color:var(--white);font-size:26px}
.slide-quote{left:183px;top:170px;width:560px;font-family:"Noto Serif",Georgia,serif;font-style:italic;color:var(--white);font-size:19px;line-height:27px}
.slide-quote b{font-style:normal;font-weight:400;font-size:21px}
.slide-arrow{top:227px;width:38px;height:38px;border-radius:50%;background:linear-gradient(#fff,#cfcfcf)}
.dots{left:544px;top:396px;display:flex;gap:7px}
.dots i{width:11px;height:11px;border-radius:50%;background:radial-gradient(#aaa,#555);display:block}
.dots i.on{background:radial-gradient(#e0323a,var(--deep-red))}

.content{left:0;top:430px;width:1182px;height:479px;background:linear-gradient(var(--white),var(--light) 85%,#e8e8e8)}
.content-cap{left:108px;top:418px;width:966px;height:60px;background:var(--white);border-radius:46px 46px 0 0}
.intro{left:173px;top:446px;width:660px;font-family:"Noto Serif",Georgia,serif;color:#666;font-size:24.5px;line-height:28px}
.learn-big{left:835px;top:440px;width:181px;height:62px;border-radius:18px;background:linear-gradient(#fff,#e9e9e9);box-shadow:0 3px 6px rgba(0,0,0,.12);display:flex;align-items:center;padding-left:18px;gap:10px;font-family:"Noto Serif",Georgia,serif;font-style:italic;color:#777;font-size:22px}
.learn-big .ring{width:22px;height:22px;border-radius:50%;border:1px solid #ccc;color:var(--red);font-size:12px;font-style:normal;display:flex;align-items:center;justify-content:center}

.card{top:533px;width:272px;height:272px;border-radius:14px;background:linear-gradient(#fff 0,#f5f5f5 20%,var(--panel));box-shadow:0 4px 8px rgba(0,0,0,.12)}
.card h3{position:absolute;left:17px;top:17px;font-family:"Noto Serif",Georgia,serif;font-weight:400;color:var(--deep-red);font-size:16.5px}
.card h3 em{color:var(--pink);font-size:12px;margin-left:6px}
.card .photo{position:absolute;left:0;top:48px;width:272px;height:99px}
.card p{position:absolute;left:18px;top:168px;width:230px;color:var(--grey-text);font-size:9.6px;line-height:12px;text-align:justify}
.card .btn{position:absolute;right:8px;bottom:-6px;width:106px;height:37px;border-radius:10px;background:linear-gradient(#fff,#ececec);box-shadow:0 2px 4px rgba(0,0,0,.15);color:var(--deep-red);font-size:11.5px;display:flex;align-items:center;justify-content:center}
.tone-a{background:linear-gradient(90deg,#e9d7c8,#aecbe6 60%,#c9d8e6)}
.tone-b{background:linear-gradient(90deg,#c9c9c3,#eae8e2 50%,#bfbfba)}
.tone-c{background:linear-gradient(90deg,#e7dcd0,#f3efe9 50%,#d8b6b2)}

.footer{left:0;top:909px;width:1182px;height:244px;background:var(--dark)}
.col{top:936px}
.col h4{color:#e8e8e8;font-family:"Open Sans",Arial,sans-serif;font-weight:400;font-size:13px;margin-bottom:10px}
.col li{list-style:none;color:#f0f0f0;font-family:"Open Sans",Arial,sans-serif;font-size:11.5px;height:22px}
.divider{top:938px;width:1px;height:198px;background:#4a4a4a}
.foot-brand{left:777px;top:960px;width:355px;height:70px;display:flex;align-items:center;justify-content:center;font-family:"Noto Serif",Georgia,serif;color:var(--footer-grey);font-size:32px;letter-spacing:1px}
.contact{left:795px;top:1062px;color:#c9c9c9;font-family:"Open Sans",Arial,sans-serif;font-weight:600;font-size:12.5px;letter-spacing:4px;line-height:25.5px;white-space:nowrap}
.bottom-bar{left:0;top:1153px;width:1182px;height:47px;background:var(--darker)}
.bottom-bar a{position:absolute;top:14px;color:var(--white);font-family:"Open Sans",Arial,sans-serif;font-size:13px;text-decoration:none}
</style>
</head>
<body>
<div class="page">
  <header class="abs header"></header>
  <nav class="nav">
    <a style="left:160px">ABOUT</a>
    <a style="left:234px">PROGRAMS</a>
    <a style="left:330px">EVENTS</a>
    <a class="schedule">SCHEDULE<span>&#8964;</span></a>
    <a style="left:889px">PROMOS</a>
    <a style="left:966px">CONTACT</a>
  </nav>
  <div class="abs brand"><span class="brand-dot"></span><span class="brand-name">IRONLEAF DOJO</span></div>

  <div class="abs slider-frame"></div>
  <div class="abs slider-mat"></div>
  <div class="abs slide-photo" role="img" aria-label="Karate student performing a flying kick against a blue sky with clouds"></div>
  <h1 class="abs slide-title" style="font-weight:400">A Model Approach To Traditional Training</h1>
  <p class="abs slide-quote">“I am developing a good fundation for effective self-defence from practical standpoint” <b>- Marlo Vance</b></p>
  <svg class="abs slide-arrow" style="left:130px" viewBox="0 0 38 38"><path d="M22 12 L14 19 L22 26" fill="none" stroke="#3c5a7a" stroke-width="3"/></svg>
  <svg class="abs slide-arrow" style="left:1014px" viewBox="0 0 38 38"><path d="M16 12 L24 19 L16 26" fill="none" stroke="#3c5a7a" stroke-width="3"/></svg>
  <div class="abs dots"><i></i><i></i><i></i><i class="on"></i><i></i></div>

  <section class="abs content"></section>
  <div class="abs content-cap"></div>
  <p class="abs intro">An academy is, according to one definition, a "meeting of persons, writers, scientists or artists" sharing something.</p>
  <div class="abs learn-big"><span class="ring">&#8250;</span>Learn more</div>

  <article class="abs card" style="left:165px">
    <h3>Pre-school and Youth<em>Material Arts</em></h3>
    <div class="photo tone-a" role="img" aria-label="Young children in white uniforms bowing in class"></div>
    <p>Praesent convallis mi id eros sodales sed sceleris-que nibh porta. Sed neque purus, consequat ac scelerisque ut, mattis tempus sapien. Suspendisse potenti.</p>
    <span class="btn">LEARN MORE</span>
  </article>
  <article class="abs card" style="left:454px">
    <h3>Adult<em>Material Arts</em></h3>
    <div class="photo tone-b" role="img" aria-label="Adult students training together in a bright dojo"></div>
    <p>Praesent convallis mi id eros sodales sed sceleris-que nibh porta. Sed neque purus, consequat ac scelerisque ut, mattis tempus sapien. Suspendisse potenti.</p>
    <span class="btn">LEARN MORE</span>
  </article>
  <article class="abs card" style="left:745px">
    <h3>Cardio<em>Kickboxing</em></h3>
    <div class="photo tone-c" role="img" aria-label="Instructor leading a group exercise on mats"></div>
    <p>Praesent convallis mi id eros sodales sed sceleris-que nibh porta. Sed neque purus, consequat ac scelerisque ut, mattis tempus sapien. Suspendisse potenti.</p>
    <span class="btn">LEARN MORE</span>
  </article>

  <footer class="abs footer"></footer>
  <div class="abs col" style="left:175px"><h4>CATEGORIES</h4><ul><li>This is a list item</li><li>This is a list item</li><li>This is a list item</li><li>This is a list item</li><li>This is a list item</li><li>This is a list item</li><li>This is a list item</li></ul></div>
  <div class="abs divider" style="left:309px"></div>
  <div class="abs col" style="left:320px"><h4>LATEST POSTS</h4><ul><li>This is a list item</li><li>This is a list item</li><li>This is a list item</li><li>This is a list item</li><li>This is a list item</li><li>This is a list item</li><li>This is a list item</li></ul></div>
  <div class="abs divider" style="left:455px"></div>
  <div class="abs col" style="left:467px"><h4>LINKS</h4><ul><li>This is a list item</li><li>This is a list item</li><li>This is a list item</li><li>This is a list item</li><li>This is a list item</li><li>This is a list item</li><li>This is a list item</li></ul></div>
  <div class="abs divider" style="left:591px"></div>
  <div class="abs col" style="left:605px"><h4>MISCELLANOUS</h4><ul><li>This is a list item</li><li>This is a list item</li><li>This is a list item</li><li>This is a list item</li><li>This is a list item</li><li>This is a list item</li><li>This is a list item</li></ul></div>
  <div class="abs foot-brand">IRONLEAF DOJO</div>
  <div class="abs contact">Phone &nbsp;: 00 00 512 0147<br>Email &nbsp;&nbsp;: info@ironleafdojo.com<br>Adress : 12 linden row north</div>

  <nav class="abs bottom-bar">
    <a style="left:175px">HOME</a>
    <a style="left:236px">ABOUT</a>
    <a style="left:303px">PROGRAMS</a>
    <a style="left:392px">EVENTS</a>
    <a style="left:462px">SCHEDULE</a>
    <a style="left:555px">PROMOS</a>
    <a style="left:631px">CONTACT</a>
  </nav>
</div>
</body>
</html>
```